Steel Company / Iron Railing Business Card Template

We are a custom steel fabrication company located in Harlow Bend, PA. In business since 1979, we recently developed a new logo, and we're looking for a business card design to help display the new logo and our business. The name of the company is Kelbrook Forge Co.. The Office Phone number is (610) 555-0143. We fabricate and install custom "wrought iron" railings on our residential side, we also fabricate and erect structural steel (think cranes and steel beams in buildings) on our commercial side. Looking to get a business card template designed. Something modern, but professional. Clear and easy to read. Front should have all business and employee information including phone number(s), email address, business information, etc. back should spotlight logo.

Industry/Entity Type

Construction / Home Improvement

Contact Information for Business Card

Business information is Kelbrook Forge Co., 48 Dunmore Ave Suite 3305, Harlow Bend, PA 19074. Phone number is (610) 555-0143. Website is www.kelbrookforge.example Business card should be for "Tom Pelling" with the job title "Sales & Estimating" but be editable for other employees. Tom's phone number is (610) 555-0178

Colors

Designer to choose colors to be used in the design.

Requirements
Must have
• Modern Feel, Design should be sized for standard business card sizing 3.5" x 2" (88.9mm x 50.8mm)

```html
<!DOCTYPE html>
<html lang="en">
<head>
<meta charset="utf-8">
<title>Kelbrook Forge Co. – Business Card</title>
<link rel="stylesheet" href="https://fonts.googleapis.com/css2?family=Montserrat:wght@500;600;700;800&display=swap">
<style>
  :root {
    --page-bg: #d9d9d9;
    --card-dark: #2b2b2b;
    --card-dark-edge: #232323;
    --card-light: #ffffff;
    --navy: #1d3a7a;
    --red: #d2232a;
    --white: #ffffff;
  }
  * { box-sizing: border-box; margin: 0; padding: 0; }
  html, body {
    width: 1200px; height: 900px; overflow: hidden;
    background: var(--page-bg);
    font-family: "Montserrat", Arial, sans-serif;
  }
  .canvas { position: relative; width: 1200px; height: 900px; }

  .card {
    position: absolute;
    width: 640px; height: 366px;
    border-radius: 3px;
    box-shadow: 0 10px 28px rgba(0,0,0,0.28);
    overflow: hidden;
  }

  /* Back of card */
  .card-back { left: 220px; top: 52px; background: var(--card-dark); }
  .card-back .pattern-area {
    position: absolute; inset: 0;
    background: linear-gradient(135deg, #333 0%, var(--card-dark) 50%, var(--card-dark-edge) 100%);
  }
  .card-back .brand-mark {
    position: absolute; left: 50%; top: 50%;
    transform: translate(-50%, -50%);
    display: flex; align-items: center; gap: 14px;
  }
  .brand-dot { width: 16px; height: 16px; border-radius: 50%; flex: none; }
  .card-back .brand-dot { background: var(--white); }
  .card-back .brand-name {
    color: var(--white); font-weight: 700; font-size: 34px; letter-spacing: 0.5px;
    white-space: nowrap;
  }

  /* Front of card */
  .card-front { left: 340px; top: 482px; background: var(--card-light); }
  .card-front .brand-block {
    position: absolute; left: 0; top: 0; width: 330px; height: 100%;
    display: flex; align-items: center; justify-content: center; gap: 10px;
  }
  .card-front .brand-dot { width: 14px; height: 14px; background: var(--red); }
  .card-front .brand-name {
    color: var(--navy); font-weight: 800; font-size: 25px; white-space: nowrap;
  }
  .divider {
    position: absolute; left: 338px; top: 70px; width: 2px; height: 226px;
    background: var(--navy);
  }
  .contact {
    position: absolute; left: 368px; top: 72px; width: 256px;
    color: var(--navy); font-weight: 600;
  }
  .contact .person-name { font-size: 16px; letter-spacing: 0.3px; text-transform: uppercase; }
  .contact .person-title { font-size: 15px; color: var(--red); margin-top: 1px; }
  .contact .phones { margin-top: 22px; }
  .phone-line { display: flex; align-items: center; gap: 8px; font-size: 16px; line-height: 1.3; }
  .phone-line svg { width: 14px; height: 16px; fill: none; stroke: var(--red); stroke-width: 2; }
  .phone-line svg.icon-office { fill: var(--red); stroke: none; }
  .address { margin-top: 22px; font-size: 15px; line-height: 1.35; }
  .website { font-size: 15px; color: var(--red); letter-spacing: 0.3px; margin-top: 2px; white-space: nowrap; }
</style>
</head>
<body>
<main class="canvas">

  <section class="card card-back" aria-label="Card back">
    <div class="pattern-area" role="img" aria-label="Repeating railing pattern in dark grey tones"></div>
    <div class="brand-mark">
      <span class="brand-dot"></span>
      <span class="brand-name">Kelbrook Forge Co.</span>
    </div>
  </section>

  <section class="card card-front" aria-label="Card front">
    <div class="brand-block">
      <span class="brand-dot"></span>
      <span class="brand-name">Kelbrook Forge Co.</span>
    </div>
    <div class="divider"></div>
    <div class="contact">
      <p class="person-name">Tom Pelling</p>
      <p class="person-title">Sales &amp; Estimating</p>
      <div class="phones">
        <p class="phone-line">
          <svg class="icon-mobile" viewBox="0 0 14 16" aria-hidden="true"><rect x="3" y="1" width="8" height="14" rx="1.5"/></svg>
          (610) 555-0178
        </p>
        <p class="phone-line">
          <svg class="icon-office" viewBox="0 0 14 16" aria-hidden="true"><path d="M1 7c0-2 2.5-3.5 6-3.5S13 5 13 7v1.2h-3V6.8c-2-.5-4-.5-6 0v1.4H1z"/><path d="M3 9.5h8l1 3.5H2z"/></svg>
          (610) 555-0143
        </p>
      </div>
      <p class="address">48 Dunmore Ave Suite 3305<br>Harlow Bend, PA 19074</p>
      <p class="website">www.kelbrookforge.example</p>
    </div>
  </section>

</main>
</body>
</html>
```